One page promotional flyer

Wanting a modern one page promotional flyer to promote our fire protection equipment and services . You can use stock images if desired .
Links to both from website below :

https://kvt-halvick.com/fire-protection/
https://kvt-halvick.com/fire-pump-service/

TY!

```html
<!DOCTYPE html>
<html lang="en">
<head>
<meta charset="utf-8">
<title>KVT Fire Protection Equipment Flyer</title>
<link href="https://fonts.googleapis.com/css2?family=Teko:wght@500;600&family=Roboto:wght@300;400;500;700&display=swap" rel="stylesheet">
<style>
  :root{
    --blue:#1450a3;
    --blue-deep:#0d3f8a;
    --blue-bright:#2a86d6;
    --ink:#111111;
    --body:#2a2a2a;
    --paper:#ffffff;
    --rule:#1d56a8;
  }
  html,body{margin:0;padding:0;overflow:hidden;}
  body{width:965px;height:1200px;background:var(--paper);}
  .flyer{position:relative;width:965px;height:1200px;overflow:hidden;background:var(--paper);font-family:'Roboto',sans-serif;color:var(--body);}
  .shapes{position:absolute;inset:0;}
  .brand{position:absolute;left:40px;top:196px;display:flex;align-items:center;gap:12px;}
  .brand-dot{width:22px;height:22px;border-radius:50%;background:var(--blue);}
  .brand-name{font-family:'Teko',sans-serif;font-weight:600;font-size:88px;line-height:1;color:var(--blue);letter-spacing:2px;}
  .headline{position:absolute;left:36px;top:334px;margin:0;font-family:'Teko',sans-serif;font-weight:600;font-size:92px;line-height:75px;color:var(--ink);letter-spacing:0.5px;}
  .headline .accent{color:var(--blue);}
  .intro{position:absolute;left:36px;top:581px;width:400px;font-weight:300;font-size:17px;line-height:21.5px;color:var(--body);}
  .intro p{margin:0 0 16px;}
  .service-title{position:absolute;left:518px;top:398px;margin:0;font-family:'Teko',sans-serif;font-weight:600;font-size:50px;line-height:1;color:var(--blue);}
  .service-text{position:absolute;left:518px;top:456px;width:380px;margin:0;font-weight:300;font-size:16.5px;line-height:21px;}
  .services-title{position:absolute;left:518px;top:540px;margin:0;font-family:'Teko',sans-serif;font-weight:600;font-size:56px;line-height:1;color:var(--ink);}
  .services{position:absolute;left:518px;top:598px;width:382px;margin:0;padding:0;list-style:none;}
  .services li{position:relative;display:flex;align-items:center;height:61px;border-bottom:1.5px solid var(--rule);padding-left:42px;font-weight:500;font-size:16.5px;line-height:20px;color:var(--ink);box-sizing:border-box;}
  .services li:last-child{border-bottom:none;}
  .services li svg{position:absolute;left:0;top:50%;margin-top:-12px;}
  .services .brand-ref{color:var(--blue);}
  .contact{position:absolute;right:128px;top:990px;text-align:right;}
  .contact-title{margin:0;font-family:'Teko',sans-serif;font-weight:600;font-size:48px;line-height:44px;color:var(--blue);}
  .contact-phone{position:absolute;left:519px;top:1036px;font-weight:700;font-size:36px;letter-spacing:3px;color:var(--ink);}
  .contact-mail{position:absolute;left:540px;top:1081px;width:300px;font-weight:500;font-size:17px;color:var(--blue);}
  .contact-web{position:absolute;left:540px;top:1104px;font-weight:300;font-style:italic;font-size:16px;letter-spacing:1px;color:var(--ink);}
</style>
</head>
<body>
<div class="flyer">
  <svg class="shapes" viewBox="0 0 965 1200" width="965" height="1200" aria-hidden="false">
    <defs>
      <linearGradient id="photoTone" x1="0" y1="0" x2="1" y2="1">
        <stop offset="0" stop-color="#3a3f47"/>
        <stop offset="0.45" stop-color="#c8232a"/>
        <stop offset="0.8" stop-color="#e23a35"/>
        <stop offset="1" stop-color="#c9d64a"/>
      </linearGradient>
      <linearGradient id="pumpTone" x1="0" y1="0" x2="1" y2="1">
        <stop offset="0" stop-color="#d8222a"/>
        <stop offset="0.6" stop-color="#e53a35"/>
        <stop offset="1" stop-color="#f3d6d6"/>
      </linearGradient>
      <linearGradient id="swooshTone" x1="0" y1="0" x2="1" y2="1">
        <stop offset="0" stop-color="#2a86d6"/>
        <stop offset="1" stop-color="#0d3f8a"/>
      </linearGradient>
    </defs>

    <!-- top photo with blue framing curve -->
    <path d="M194 0 C235 140 310 250 405 310 C560 365 790 380 965 365 L965 0 Z" fill="var(--blue)"/>
    <path d="M240 0 C280 130 350 230 438 295 C590 350 790 362 965 348 L965 0 Z" fill="url(#photoTone)" role="img" aria-label="Photo: technicians servicing a red fire pump installation"/>

    <!-- vertical blue band -->
    <path d="M405 310 C440 330 455 360 462 400 C480 520 502 640 490 760 C478 900 430 1080 373 1200 L445 1200 C490 1070 510 900 508 760 C506 640 492 520 476 420 C470 385 462 350 445 325 Z" fill="var(--blue)"/>

    <!-- bottom left product image -->
    <path d="M0 860 L413 860 L413 1080 C395 1130 380 1170 365 1200 L0 1200 Z" fill="url(#pumpTone)" role="img" aria-label="Photo: red end-suction fire pump with motor on a steel base"/>

    <!-- contact swoosh -->
    <path d="M776 975 C860 955 925 970 912 1020 C895 1090 760 1165 640 1155 C612 1152 600 1142 604 1128 C612 1150 650 1155 690 1148 C790 1130 880 1070 893 1020 C902 985 850 968 776 975 Z" fill="url(#swooshTone)"/>
  </svg>

  <div class="brand">
    <span class="brand-dot"></span>
    <span class="brand-name">KVT</span>
  </div>

  <h1 class="headline">FIRE<br><span class="accent">PROTECTION</span><br>EQUIPMENT</h1>

  <div class="intro">
    <p>Ridgeline Pump designs tough, versatile products to meet your pumping needs. The fire pump units, systems, and housed packaged systems offer variety, durability, standardized options and configurations true to their outstanding reputation.</p>
    <p>Thousands of Ridgeline Pump installations (UL, ULC, or FM approved) deliver superior fire protection to facilities worldwide. Products are designed from a broad selection of pumps, drives, controls, baseplates and accessories.</p>
  </div>

  <h2 class="service-title">Fire Pump Service</h2>
  <p class="service-text">Our technicians are well versed in every fire pump make and model and the fire pump parts associated with any repair.</p>

  <h2 class="services-title">Our Services Include:</h2>
  <ul class="services">
    <li><svg width="28" height="24" viewBox="0 0 28 24"><path d="M3 12 L9 18 L18 3" fill="none" stroke="var(--blue)" stroke-width="2.4" stroke-linecap="round" stroke-linejoin="round"/><path d="M20 8 C27 12 20 22 10 21" fill="none" stroke="var(--blue)" stroke-width="2" stroke-linecap="round"/></svg>Fire pump repacks / overhaul / testing<br>*most fire pump manufacturers</li>
    <li><svg width="28" height="24" viewBox="0 0 28 24"><path d="M3 12 L9 18 L18 3" fill="none" stroke="var(--blue)" stroke-width="2.4" stroke-linecap="round" stroke-linejoin="round"/><path d="M20 8 C27 12 20 22 10 21" fill="none" stroke="var(--blue)" stroke-width="2" stroke-linecap="round"/></svg>Control panel troubleshooting and<br>repair (common makes and models)</li>
    <li><svg width="28" height="24" viewBox="0 0 28 24"><path d="M3 12 L9 18 L18 3" fill="none" stroke="var(--blue)" stroke-width="2.4" stroke-linecap="round" stroke-linejoin="round"/><path d="M20 8 C27 12 20 22 10 21" fill="none" stroke="var(--blue)" stroke-width="2" stroke-linecap="round"/></svg>Motor repair and replacement</li>
    <li><svg width="28" height="24" viewBox="0 0 28 24"><path d="M3 12 L9 18 L18 3" fill="none" stroke="var(--blue)" stroke-width="2.4" stroke-linecap="round" stroke-linejoin="round"/><path d="M20 8 C27 12 20 22 10 21" fill="none" stroke="var(--blue)" stroke-width="2" stroke-linecap="round"/></svg><span>In-stock fire pump parts for all <span class="brand-ref">Ridgeline / Norvik</span> pumps</span></li>
    <li><svg width="28" height="24" viewBox="0 0 28 24"><path d="M3 12 L9 18 L18 3" fill="none" stroke="var(--blue)" stroke-width="2.4" stroke-linecap="round" stroke-linejoin="round"/><path d="M20 8 C27 12 20 22 10 21" fill="none" stroke="var(--blue)" stroke-width="2" stroke-linecap="round"/></svg>Jockey pumps and jockey pump<br>controllers in stock</li>
    <li><svg width="28" height="24" viewBox="0 0 28 24"><path d="M3 12 L9 18 L18 3" fill="none" stroke="var(--blue)" stroke-width="2.4" stroke-linecap="round" stroke-linejoin="round"/><path d="M20 8 C27 12 20 22 10 21" fill="none" stroke="var(--blue)" stroke-width="2" stroke-linecap="round"/></svg>Testing equipment: Hoses, Pitot tubes,<br>tachometers</li>
  </ul>

  <div class="contact"><h2 class="contact-title">Get In Touch</h2></div>
  <div class="contact-phone">(555)014-3200</div>
  <div class="contact-mail">sales@kvt-halvick.com</div>
  <div class="contact-web">www.kvt-halvick.com</div>
</div>
</body>
</html>
```